Media Services Start-up -- Corporate Website and Logo Design. Inspiration required!

We need a logo design and corporate website design, including coding, for our start-up business.
Varnetto’s value proposition is based on bringing together media content from a vast number of geographies globally, adding human and AI curation, translation and editing, and delivering the content using tailored customer interfaces. On the one hand, the business brings together media coverage from all over the world, and on the other it brings together content, human skills and technology to deliver a supreme customer experience.
Varnetto is a B2B media monitoring and analytics business with emphasis on global customers. Varnetto's service offering is centred around sourcing media content from different markets, processing, storing and delivering the content and insights derived from it using an online platform / mobile app.
The messaging we want to create through the logo is:
- Global scope
- Speed of delivery
- Cost-efficiency
- Multi-lingual
- Tailor-made
- Trustworthy
Target Market(s)
Business to business, PR / Communications, Media, Marketing
Logo Text
Varnetto
Coding
Coded - Design and coding required
Number of Pages Required
5+ page
Font styles to use
Other font styles liked:
- See Design Brief for details
Colors
Designer to choose colors to be used in the design.

```html
<!DOCTYPE html>
<html lang="en">
<head>
<meta charset="utf-8">
<title>Varnetto — Global Media Intelligence</title>
<link rel="stylesheet" href="https://fonts.googleapis.com/css2?family=Roboto:wght@400;500;700&family=Poppins:wght@400;500&display=swap">
<style>
:root{
  --red:#f55656;
  --ink:#1d1d1d;
  --text:#333;
  --white:#fff;
  --canvas:#ececec;
  --photo-dark:#1b2634;
  --photo-mid:#3c5168;
  --photo-blue:#6c9fc8;
}
*{box-sizing:border-box;margin:0;padding:0}
html,body{width:1200px;height:3277px;overflow:hidden}
body{background:linear-gradient(var(--canvas) 0,var(--canvas) 2482px,var(--white) 2482px);font-family:"Roboto",sans-serif;color:var(--text);position:relative}
.page{position:absolute;left:46px;width:1108px;background:var(--white);box-shadow:0 1px 6px rgba(0,0,0,.12)}
.page--home{top:23px;height:770px}
.page--solution{top:821px;height:2382px}

.site-header{position:relative;height:108px}
.brand{position:absolute;left:83px;top:30px;font:700 41px/1 "Roboto",sans-serif;color:var(--red)}
.nav-item{position:absolute;top:29px;color:var(--red);font-weight:700;font-size:20px;line-height:1}
.nav-item small{display:block;margin-top:9px;font-size:12.5px;color:var(--ink)}
.nav-item--monitor{left:365px}
.nav-item--about{left:658px;top:43px}
.nav-item--demo{left:794px}
.nav-item--phone{left:883px}

.hero{position:absolute;left:0;top:108px;width:1108px;overflow:hidden}
.hero__photo{position:absolute;inset:0;background:linear-gradient(100deg,var(--photo-dark) 0%,var(--photo-mid) 45%,#2a3a4c 70%,#4a4a3e 100%)}
.hero__shade{position:absolute;inset:0;background:linear-gradient(90deg,rgba(10,15,25,.55),rgba(10,15,25,.15))}
.page--home .hero{height:662px}
.page--solution .hero{height:331px}

.hero__title{position:absolute;left:85px;top:228px;width:500px;color:var(--white);font-size:33px;font-weight:700;line-height:49px}
.hero__lead{position:absolute;left:85px;top:338px;width:475px;color:var(--white);font-size:14.5px;line-height:33px}
.hero__legal{position:absolute;left:0;right:0;top:632px;text-align:center;color:var(--white);font-size:13.5px}

.quote-form{position:absolute;left:583px;top:123px;width:442px;height:416px;background:rgba(240,240,242,.9)}
.quote-form h2{position:absolute;left:0;right:0;top:36px;text-align:center;color:var(--red);font-size:25px;font-weight:700}
.field{position:absolute;left:27px;width:388px;height:32px;background:var(--white);border:1px solid #cfcfcf;font:400 13px/30px "Poppins",sans-serif;color:#888;padding-left:30px}
.field svg{position:absolute;left:11px;top:9px}
.field--msg{height:74px}
.submit{position:absolute;left:27px;top:332px;width:388px;height:41px;background:var(--red);color:var(--white);font:500 15px/41px "Poppins",sans-serif;text-align:center}
.submit svg{vertical-align:-2px;margin-right:6px}

.hero__heading{position:absolute;right:84px;top:124px;color:var(--white);font-size:41px;font-weight:700}

.sourcing-visual{position:absolute;left:55px;top:518px;width:436px;height:467px;background:var(--red)}
.sourcing-visual__photo{position:absolute;left:18px;top:30px;width:436px;height:467px;background:linear-gradient(160deg,#cfe6f6 0%,var(--photo-blue) 45%,#2e5e86 100%)}

.section-title{color:var(--red);font-size:33px;font-weight:700;line-height:1}
.sourcing{position:absolute;left:535px;top:522px;width:492px}
.sourcing__lead{margin-top:12px;color:var(--ink);font-size:20px;font-weight:500;line-height:41px}
.sourcing .points{margin-top:13px;font-size:13.5px}

.points{list-style:none;font-size:16px;line-height:41px;color:var(--ink)}
.points li.plain::before{display:none}
.points li::before{content:"→";display:inline-block;width:14px;height:14px;border:1.5px solid var(--red);border-radius:50%;color:var(--red);font-size:10px;line-height:11px;text-align:center;font-weight:700;margin-right:7px;vertical-align:1px}
.points .strong{font-weight:700}

.block{position:absolute;left:80px;width:980px}
.block .points{margin-top:14px;padding-left:5px}
.block--collection{top:1104px}
.block--augmentation{top:1262px}
.block--delivery{top:1626px}
.block--insights{top:1903px}

.site-footer{position:absolute;left:0;bottom:0;width:1108px;height:83px;background:var(--red);color:var(--white);text-align:center;font-size:13.5px;line-height:83px}
</style>
</head>
<body>

<section class="page page--home">
  <header class="site-header">
    <div class="brand">Varnetto</div>
    <div class="nav-item nav-item--monitor">MONITORING &amp; INSIGHTS<small>Across Print, Online, TV, Radio and Social</small></div>
    <div class="nav-item nav-item--about">ABOUT US</div>
    <div class="nav-item nav-item--demo">DEMO<small>Start now</small></div>
    <div class="nav-item nav-item--phone">(02) 5550 1842<small>Talk to us today</small></div>
  </header>
  <div class="hero">
    <div class="hero__photo" role="img" aria-label="Photo of an analyst at a desk viewing a world map and market charts on a glass screen"></div>
    <div class="hero__shade"></div>
    <h1 class="hero__title">DELIVERING GLOBAL MEDIA INTELLIGENCE</h1>
    <p class="hero__lead">Varnetto is an international media intelligence service provider. We help communications teams build and operate truly global media monitoring and measurement programmes.</p>
    <form class="quote-form">
      <h2>GET A FREE QUOTE</h2>
      <div class="field" style="top:83px"><svg width="11" height="11" viewBox="0 0 10 10"><circle cx="5" cy="3" r="2.5" fill="#888"/><path d="M0 10c0-3 2-4.5 5-4.5s5 1.5 5 4.5z" fill="#888"/></svg>First Name</div>
      <div class="field" style="top:124px"><svg width="11" height="11" viewBox="0 0 10 10"><circle cx="5" cy="3" r="2.5" fill="#888"/><path d="M0 10c0-3 2-4.5 5-4.5s5 1.5 5 4.5z" fill="#888"/></svg>Last Name</div>
      <div class="field" style="top:165px"><svg width="12" height="10" viewBox="0 0 12 10"><rect width="12" height="10" rx="1" fill="#888"/><path d="M0 1l6 4 6-4" stroke="#fff" fill="none"/></svg>Email</div>
      <div class="field" style="top:206px"><svg width="11" height="11" viewBox="0 0 10 10"><path d="M2 0l2 2.5-1.2 1.3a6 6 0 003.4 3.4L7.5 6 10 8l-1 2C4 10 0 6 0 1z" fill="#888"/></svg>Phone</div>
      <div class="field field--msg" style="top:247px"><svg width="12" height="10" viewBox="0 0 12 10"><ellipse cx="5" cy="4" rx="5" ry="3.5" fill="#888"/><ellipse cx="8" cy="6" rx="4" ry="3" fill="#888"/></svg>Message</div>
      <div class="submit"><svg width="11" height="13" viewBox="0 0 11 13"><path d="M0 0h7l4 4v9H0z" fill="#fff"/></svg>SUBMIT</div>
    </form>
    <p class="hero__legal">Copyrights © 2019. All Rights Reserved.</p>
  </div>
</section>

<section class="page page--solution">
  <header class="site-header">
    <div class="brand">Varnetto</div>
    <div class="nav-item nav-item--monitor">MONITORING &amp; INSIGHTS<small>Across Print, Online, TV, Radio and Social</small></div>
    <div class="nav-item nav-item--about">ABOUT US</div>
    <div class="nav-item nav-item--demo">DEMO<small>Start now</small></div>
    <div class="nav-item nav-item--phone">(02) 5550 1842<small>Talk to us today</small></div>
  </header>
  <div class="hero">
    <div class="hero__photo" role="img" aria-label="Photo of an analyst at a desk viewing a world map and market charts on a glass screen"></div>
    <div class="hero__shade"></div>
    <h1 class="hero__heading">Our Solution</h1>
  </div>

  <div class="sourcing-visual">
    <div class="sourcing-visual__photo" role="img" aria-label="Illustration of a businessman facing a large screen of world map and data charts over a city skyline"></div>
  </div>
  <div class="sourcing">
    <h2 class="section-title">Content Sourcing</h2>
    <p class="sourcing__lead">We help you build a content strategy that meets your budget and coverage needs across earned media - Print, Online, TV and Radio.</p>
    <ul class="points">
      <li>Identify geographies and markets of interest</li>
      <li class="strong">Build target media source lists to fulfil monitoring and measurement requirements</li>
      <li>Using our transparent cost calculator, we help you with accurate budgeting and choices to ensure you meet your strategy and objectives</li>
      <li>Translate and localise keyword searches and editorial instructions into efficient source-/ country-/ provider-specific needs to minimise wasted content.</li>
    </ul>
  </div>

  <div class="block block--collection">
    <h2 class="section-title">Content Collection</h2>
    <ul class="points">
      <li>We consolidate and manage the delivery of your global media content into a Cloud-based scalable media platform, taking the headache of content management away from your teams.</li>
    </ul>
  </div>

  <div class="block block--augmentation">
    <h2 class="section-title">Content Augmentation</h2>
    <ul class="points">
      <li>We manage and normalise all of the source-level reference data - country, language, reach etc.</li>
      <li>We add editorial validation to ensure only the content required reaches your delivery, removing inevitable noise from source providers</li>
      <li>Tagging - AI and human based tagging to detect locations, people, topics, products, brands, services, etc.</li>
      <li>Human and automated grouping of stories across geographies - clustering, "also-in" groupings etc.</li>
      <li>Translation summarisation - AI Translation or human-created depending on budget, speed of delivery and need.</li>
      <li>Digest authoring - refining the essence of today’s coverage into a concise board-ready output for your organisation</li>
    </ul>
  </div>

  <div class="block block--delivery">
    <h2 class="section-title">Content Delivery</h2>
    <ul class="points">
      <li class="plain">Early morning delivery of a consolidated, ready-to-consume media coverage</li>
      <li>Customised email templates, delivering content in templates designed to meet your needs</li>
      <li>Customised platform - modern portal tailored to meet your media management needs, removing the unwanted clutter and focusing on the job at hand</li>
      <li>Integration with Intranets, third-party communication tools e.g. ChatDesk, RSS readers, customised APIs</li>
    </ul>
  </div>

  <div class="block block--insights">
    <h2 class="section-title">Media Insights &amp; Consultancy</h2>
    <ul class="points">
      <li>Levering the normalised content sets from your integrated monitoring service, we can analyse and tag your coverage based on complex qualitative measurement criteria, consistent across all languages and geographies, to combine with quantitative metrics.</li>
      <li>Ability to create a single consistent measurement programme across all of your global operations.</li>
      <li>Consultancy to HQ and local offices on how to utilise and align existing measurement and insight intiatives to provide continuity.</li>
      <li>Customised online dashboards with near real time data insights, coupled with Board-ready offline reporting and export options.</li>
      <li>Integration with social media content, third-party data, point-of-sale, WebMetric Analytics, and delivering on your Integrated Communications Framework</li>
    </ul>
  </div>

  <footer class="site-footer">Copyrights © 2019. All Rights Reserved.</footer>
</section>

</body>
</html>
```